3D Printing Business coming soon page

Hi we are looking for a one page "coming soon" website for our business. The business is called "Solevia Labs" and it is a new solution which 3D Prints Orthotics (Insoles).

The design should include our logo, an improved version of our promotional image (attached), a web form for capturing interest from people, a countdown timer and some text.

Follow the colour scheme which is shown in our logo along with our other colours - Orange (RGB#ff8300) and Light Green (RGB#30f20a)
Updates

Industry/Entity Type

Business

Font styles to use
Sans Serif

Requirements
Must have
• Logo (Attached)
Improved version of Promotional Image
Web Form design for capturing Name, EMail Address and Comments along with a Turin test
Countdown Timer
Text - "Solevia Labs will shake up the Orthotics Industry. Foot Orthosis patient-ready in hours for a fraction of the price you are paying today. Welcome to the new world of 3D Printing!"

```html
<!DOCTYPE html>
<html lang="en">
<head>
<meta charset="utf-8">
<title>Solevia Labs — Coming Soon</title>
<link rel="stylesheet" href="https://fonts.googleapis.com/css2?family=Lato:wght@300;400;700;900&display=swap">
<style>
:root{
  --orange:#ff8300;
  --green:#30f20a;
  --green-deep:#2fd214;
  --navy:#263466;
  --brand-blue:#1f62a3;
  --ink:#2a2a2a;
  --muted:#c4c4c4;
  --panel:#ededed;
  --field-border:#cfcfcf;
  --footer-text:#8a8a8a;
}
*{box-sizing:border-box;margin:0;padding:0}
html,body{width:1200px;height:743px;overflow:hidden}
body{
  position:relative;
  font-family:"Lato",sans-serif;
  background:radial-gradient(ellipse at 50% 35%,#ffffff 0%,#f7f7f7 55%,#ececec 100%);
  color:var(--ink);
}
.abs{position:absolute}

/* hero */
.hero-title{left:230px;width:390px;top:34px;text-align:center;font-weight:900;font-size:43px;letter-spacing:-2px;color:var(--orange)}
.brand{left:268px;width:320px;top:150px;display:flex;align-items:center;justify-content:center;gap:12px}
.brand-mark{width:34px;height:34px;border-radius:50%;background:var(--brand-blue)}
.brand-name{font-weight:900;font-size:40px;letter-spacing:-1px;color:var(--brand-blue)}
.countdown-label{left:230px;width:400px;top:301px;text-align:center;font-weight:900;font-size:19.5px;letter-spacing:-1px;color:var(--muted)}
.countdown{left:307px;top:330px;display:flex;gap:7px}
.tile{width:56px;height:61px;border-radius:3px;background:linear-gradient(#3ff01c,var(--green-deep));color:#fff;text-align:center;padding-top:8px}
.tile-num{font-weight:400;font-size:31px;line-height:1}
.tile-unit{font-weight:700;font-size:6.5px;letter-spacing:.3px;margin-top:7px}

/* contact panel */
.contact{left:674px;top:28px;width:290px;height:394px;background:var(--panel)}
.contact-kicker{left:0;width:290px;top:14px;text-align:center;font-weight:900;font-size:19.5px;letter-spacing:-1px;color:var(--navy)}
.contact-title{left:0;width:290px;top:30px;text-align:center;font-weight:900;font-size:43px;letter-spacing:-2px;color:var(--navy)}
.field{background:#fff;border:1px solid var(--field-border);border-radius:2px;font-size:11.5px;color:var(--navy);padding:11px 15px}
.field-name{left:16px;top:82px;width:250px;height:35px}
.field-email{left:16px;top:126px;width:250px;height:35px}
.field-message{left:16px;top:167px;width:250px;height:115px}
.field-icon{position:absolute;right:10px;top:8px}
.captcha{left:16px;top:287px;width:100px;height:35px;border:1px solid var(--field-border);border-radius:2px;background:linear-gradient(#fafafa,#e8e8e8)}
.captcha-input{left:119px;top:287px;width:147px;height:35px;background:#fff;border:1px solid var(--field-border);border-radius:2px}
.submit{left:18px;top:330px;width:248px;height:33px;background:var(--green);color:#fff;font-weight:900;font-size:19.5px;letter-spacing:-1px;text-align:center;line-height:33px}

/* process band */
.process{left:0;top:416px;width:1200px;height:181px;background:var(--navy)}
.step-title{width:200px;text-align:center;top:32px;color:#fff;font-size:17.5px;font-weight:400}
.step-num{top:90px;color:var(--green);font-size:28px;font-weight:300}
.step-arrow{top:86px}
.step-image{border-radius:2px}

/* pitch + footer */
.pitch{left:150px;width:900px;top:614px;text-align:center;font-weight:300;font-size:17.5px;line-height:22px;color:#1e1e1e}
.rule{left:198px;top:689px;width:801px;height:1px;background:#cccccc}
.copyright{left:199px;top:711px;font-size:10.5px;color:var(--footer-text)}
.social{left:900px;width:100px;top:706px;display:flex;justify-content:flex-end;gap:10px;font-size:10px;font-weight:700;color:#9a9a9a}
</style>
</head>
<body>

<h1 class="abs hero-title">COMING SOON</h1>

<div class="abs brand">
  <span class="brand-mark"></span>
  <span class="brand-name">Solevia Labs</span>
</div>

<p class="abs countdown-label">COUNT DOWN STARTS NOW!</p>
<div class="abs countdown">
  <div class="tile"><div class="tile-num">16</div><div class="tile-unit">DAYS</div></div>
  <div class="tile"><div class="tile-num">23</div><div class="tile-unit">HOURS</div></div>
  <div class="tile"><div class="tile-num">45</div><div class="tile-unit">MINUTES</div></div>
  <div class="tile"><div class="tile-num">67</div><div class="tile-unit">SECONDS</div></div>
</div>

<section class="abs contact">
  <p class="abs contact-kicker">IF YOU HAVE A QUESTION?</p>
  <h2 class="abs contact-title">CONTACT US</h2>
  <div class="abs field field-name">Name
    <svg class="field-icon" width="18" height="20" viewBox="0 0 18 20"><circle cx="9" cy="6" r="5" fill="#d4d4d4"/><path d="M0 20c0-6 4-8 9-8s9 2 9 8z" fill="#d4d4d4"/></svg>
  </div>
  <div class="abs field field-email">Email
    <svg class="field-icon" width="20" height="14" viewBox="0 0 20 14"><rect width="20" height="14" rx="1" fill="#d4d4d4"/><path d="M1 1l9 7 9-7" stroke="#fff" stroke-width="1.2" fill="none"/></svg>
  </div>
  <div class="abs field field-message">Message
    <svg class="field-icon" width="20" height="20" viewBox="0 0 20 20"><path d="M3 17l1-5 10-10 4 4-10 10z" fill="none" stroke="#cfcfcf" stroke-width="1.6"/></svg>
  </div>
  <div class="abs captcha" role="img" aria-label="Distorted verification word"></div>
  <div class="abs captcha-input"></div>
  <div class="abs submit">SUBMIT NOW!</div>
</section>

<section class="abs process">
  <h3 class="abs step-title" style="left:219px">Scan The Foot</h3>
  <h3 class="abs step-title" style="left:421px">Design The Orthotic</h3>
  <h3 class="abs step-title" style="left:620px">3D Print</h3>
  <h3 class="abs step-title" style="left:805px">Fit It</h3>

  <span class="abs step-num" style="left:219px">1.</span>
  <svg class="abs step-arrow" style="left:240px" width="26" height="44" viewBox="0 0 26 44"><path d="M4 3l18 19L4 41" stroke="var(--green)" stroke-width="4" fill="none"/></svg>
  <div class="abs step-image" style="left:278px;top:68px;width:82px;height:86px;background:linear-gradient(160deg,#f4f4f4,#b9b9b9)" role="img" aria-label="Tablet with a 3D scanner attached"></div>

  <span class="abs step-num" style="left:382px">2.</span>
  <svg class="abs step-arrow" style="left:405px" width="26" height="44" viewBox="0 0 26 44"><path d="M4 3l18 19L4 41" stroke="var(--green)" stroke-width="4" fill="none"/></svg>
  <div class="abs step-image" style="left:445px;top:62px;width:152px;height:100px;background:linear-gradient(#f7f7f7,#e6e2d4)" role="img" aria-label="Design software showing a foot model over an orthotic insole"></div>

  <span class="abs step-num" style="left:616px">3.</span>
  <svg class="abs step-arrow" style="left:638px" width="26" height="44" viewBox="0 0 26 44"><path d="M4 3l18 19L4 41" stroke="var(--green)" stroke-width="4" fill="none"/></svg>
  <div class="abs step-image" style="left:672px;top:64px;width:98px;height:94px;background:linear-gradient(#b73a5a,#d9d6d3 40%,#bdb8b3)" role="img" aria-label="Desktop 3D printer"></div>

  <span class="abs step-num" style="left:795px">4.</span>
  <svg class="abs step-arrow" style="left:817px" width="26" height="44" viewBox="0 0 26 44"><path d="M4 3l18 19L4 41" stroke="var(--green)" stroke-width="4" fill="none"/></svg>
  <div class="abs step-image" style="left:852px;top:72px;width:132px;height:80px;border-radius:40px;background:linear-gradient(100deg,#1c1c1c,#e9e2cf 45%,#1c1c1c)" role="img" aria-label="Hand fitting a printed insole into a shoe"></div>
</section>

<p class="abs pitch">Solevia Labs will shake up the Orthotics Industry. Foot Orthosis patient-ready in hours for a fraction<br>of the price you are paying today. Welcome to the new world of 3D Printing!</p>

<div class="abs rule"></div>
<p class="abs copyright">©2013 Solevia Labs.&nbsp;&nbsp; All rights reserved.</p>
<div class="abs social"><span>Friendly</span><span>Chirp</span><span>Worknet</span></div>

</body>
</html>
```